Upcoming lecture sponsored by a church on an important topic

We have a Reformation The Speech coming up at the end of October on the topic of law and gospel. I thought it might be cool to use a flyer that looks like it was from that day and age. Picture what Conrad Velmer would advertise things on kind of an old church/reformation type format. It will be sponsored by our church, and we have a paragraph or two to describe the lecture that would be included on the flyer. We would also want it formatted so that it could be printed on postcards and mailed to churches and individuals.

The flyer should have the following paragraph...

The distinction between the law and the gospel is the most important distinction in the Christian faith. Conrad Velmer: “Distinguishing between the law and the gospel is the highest art in Christendom, one who every person who values the name Christian ought to recognize, know, and possess.” The distinction between the law and the gospel is of great comfort for the child of God. “For the law was given by Moses, but grace and truth came by Jesus Christ” (John 1:17). For these reasons, the distinction between the law and the gospel is the most heavily assaulted doctrine in the Christian faith. This Reformation Day, join us for an explanation and defense of the great distinction between God’s good law and God’s glorious gospel.

And the flyer should have the following information...

Topic: The Steady Word and the Bright Promise
Date and Time: Tuesday, October 31, 2023 at 7:30pm
Host: Harrow Creek Fellowship Church
Speaker: Rev. Gerald Voskuil
Venue: The Marlow Hall, 5172 Brenton Avenue, Hudsonville, MI 49318
Format: Lecture followed by Q&A and refreshments

00AB8E
00BBA5
67D7C9
C6EFE9
E9F9F6

• The color scheme that I would like to have is a teal color (the same color as found at www.brackenhollowchapel.com

```html
<!DOCTYPE html>
<html lang="en">
<head>
<meta charset="utf-8">
<title>Reformation Day Lecture – Postcard Front and Back</title>
<link rel="stylesheet" href="https://fonts.googleapis.com/css2?family=EB+Garamond:ital,wght@0,400;0,500;0,600;1,400;1,500&family=Montserrat:wght@700&display=swap">
<style>
  :root {
    --ink-label: #1f4a5a;
    --band: #0f5c62;
    --sky-top: #66dcd6;
    --sky-mid: #4cc3cf;
    --sky-bottom: #1d9cab;
    --stripe-light: #3cc4cc;
    --accent: #4fd6e6;
    --quote: #3fb3c0;
    --pill: #173746;
    --text-light: #ffffff;
    --text-soft: #e4f2f2;
  }
  * { box-sizing: border-box; margin: 0; padding: 0; }
  html, body { width: 1200px; height: 779px; overflow: hidden; background: #ffffff; }
  body { position: relative; font-family: "EB Garamond", Georgia, serif; }

  .side-label {
    position: absolute;
    font-family: "Montserrat", Arial, sans-serif;
    font-weight: 700;
    font-size: 20px;
    color: var(--ink-label);
    transform: translateX(-50%);
    letter-spacing: 0.5px;
  }
  .side-label--front { left: 330px; top: 38px; }
  .side-label--back { left: 875px; top: 36px; }

  .card {
    position: absolute;
    width: 434px;
    height: 614px;
    overflow: hidden;
    background: linear-gradient(180deg, var(--sky-top) 0%, var(--sky-mid) 50%, var(--sky-bottom) 100%);
    box-shadow: 14px 16px 22px rgba(0, 0, 0, 0.22);
  }
  .card--front { left: 134px; top: 83px; }
  .card--back { left: 651px; top: 78px; }

  .stripe { position: absolute; top: 0; bottom: 0; }
  .stripe--dark-left { left: 77px; width: 5px; background: var(--band); }
  .stripe--light-left { left: 82px; width: 7px; background: var(--stripe-light); }
  .stripe--light-right { left: 348px; width: 7px; background: var(--stripe-light); }
  .stripe--dark-right { left: 355px; width: 5px; background: var(--band); }

  .column-band {
    position: absolute;
    left: 89px; width: 259px; top: 0; bottom: 0;
    background: var(--band);
  }
  .cross-band {
    position: absolute;
    left: 0; right: 0; top: 91px; height: 120px;
    background: var(--band);
  }

  .front-content {
    position: absolute;
    inset: 0;
    text-align: center;
    color: var(--text-light);
  }
  .front-content > * { position: absolute; left: 0; right: 0; }

  .headline {
    top: 22px;
    font-size: 30px;
    font-weight: 500;
    color: var(--accent);
    letter-spacing: 2px;
  }
  .field-label {
    font-style: italic;
    font-weight: 500;
    color: var(--accent);
    font-size: 13.5px;
    letter-spacing: 0.5px;
  }
  .topic-label { top: 113px; font-size: 14.5px; }
  .topic-title {
    top: 135px;
    font-size: 19.5px;
    font-weight: 600;
    letter-spacing: 2.2px;
    line-height: 26px;
    text-transform: uppercase;
  }
  .speaker-tag {
    top: 247px;
    left: 178px; right: auto;
    width: 81px; height: 18px;
    border-radius: 9px;
    background: var(--pill);
    font-style: italic;
    font-size: 14px;
    line-height: 18px;
    letter-spacing: 1px;
  }
  .speaker-name {
    top: 268px;
    font-size: 18px;
    font-weight: 500;
    letter-spacing: 1.6px;
  }
  .date-label { top: 324px; }
  .date-text, .venue-text {
    font-size: 12.5px;
    font-weight: 500;
    line-height: 19.2px;
  }
  .date-text { top: 343px; }
  .venue-label { top: 400px; }
  .venue-text { top: 419px; }
  .divider {
    top: 521px;
    left: 143px; right: auto;
    width: 138px;
    border-top: 2px dotted var(--accent);
  }
  .format-note {
    top: 535px;
    font-style: italic;
    font-size: 13px;
    line-height: 19.2px;
  }

  .quote-mark { position: absolute; left: 197px; width: 44px; height: 30px; }
  .quote-mark--open { top: 69px; }
  .quote-mark--close { top: 517px; }
  .quote-mark path { fill: var(--quote); }

  .lecture-summary {
    position: absolute;
    left: 114px; top: 115px;
    width: 207px;
    color: var(--text-soft);
    font-size: 12.6px;
    line-height: 17px;
    letter-spacing: 0.45px;
    text-align: justify;
    text-indent: 8px;
  }
</style>
</head>
<body>
  <div class="side-label side-label--front">FRONT</div>
  <div class="side-label side-label--back">BACK</div>

  <section class="card card--front">
    <div class="stripe stripe--dark-left"></div>
    <div class="stripe stripe--light-left"></div>
    <div class="stripe stripe--light-right"></div>
    <div class="stripe stripe--dark-right"></div>
    <div class="column-band"></div>
    <div class="cross-band"></div>

    <div class="front-content">
      <h1 class="headline">JOIN US !</h1>
      <p class="field-label topic-label">Topic</p>
      <h2 class="topic-title">The Steady Word and<br>the Bright Promise</h2>
      <p class="speaker-tag">Speaker</p>
      <p class="speaker-name">Rev. Gerald Voskuil</p>
      <p class="field-label date-label">Date and Time</p>
      <p class="date-text">Tuesday, October 31, 2023<br>at 7:30pm</p>
      <p class="field-label venue-label">Host &amp; Venue</p>
      <p class="venue-text">Harrow Creek Fellowship Church<br>The Marlow Hall, 5172<br>Brenton Avenue,<br>Hudsonville, MI 49318</p>
      <div class="divider"></div>
      <p class="format-note">Lecture followed by Q&amp;A<br>&amp; refreshments</p>
    </div>
  </section>

  <section class="card card--back">
    <div class="stripe stripe--dark-left"></div>
    <div class="stripe stripe--light-left"></div>
    <div class="stripe stripe--light-right"></div>
    <div class="stripe stripe--dark-right"></div>
    <div class="column-band"></div>

    <svg class="quote-mark quote-mark--open" viewBox="0 0 44 30" aria-hidden="true">
      <path d="M2 0h15a2 2 0 0 1 2 2v13a2 2 0 0 1-2 2h-7c0 5 4 9 9 11v2C9 30 0 24 0 14V2a2 2 0 0 1 2-2z"/>
      <path d="M26 0h15a2 2 0 0 1 2 2v13a2 2 0 0 1-2 2h-7c0 5 4 9 9 11v2c-10 0-19-6-19-16V2a2 2 0 0 1 2-2z"/>
    </svg>

    <p class="lecture-summary">The distinction between the law and the gospel is the most important distinction in the Christian faith. Conrad Velmer: “Distinguishing between the law and the gospel is the highest art in Christendom, one who every person who values the name Christian ought to recognize, know, and possess.” The distinction between the law and the gospel is of great comfort for the child of God. “For the law was given by Moses, but grace and truth came by Jesus Christ” (John 1:17). For these reasons, the distinction between the law and the gospel is the most heavily assaulted doctrine in the Christian faith. This Reformation Day, join us for an explanation and defense of the great distinction between God’s good law and God’s glorious gospel.</p>

    <svg class="quote-mark quote-mark--close" viewBox="0 0 44 30" aria-hidden="true">
      <path d="M42 30H27a2 2 0 0 1-2-2V15a2 2 0 0 1 2-2h7c0-5-4-9-9-11V0c10 0 19 6 19 16v12a2 2 0 0 1-2 2z"/>
      <path d="M18 30H3a2 2 0 0 1-2-2V15a2 2 0 0 1 2-2h7c0-5-4-9-9-11V0c10 0 19 6 19 16v12a2 2 0 0 1-2 2z"/>
    </svg>
  </section>
</body>
</html>
```